Need Primer (paint) Label Design

THE ATTACHED LABEL/S ARE SOLEY FOR REFERENCE. DO NOT MAKE ME AN INTERIOR PAINT OR CHALK PAINT LABEL. I ONLY NEED A "PRIMER" LABEL. THE ATTACHED INTERIOR PAINT LABEL IS ONLY TO SHOW YOU THE THEME/DESIGN OF OUR OTHER LABELS. THE BLUE LABEL ONLY HAS A DESIGN ASPECT I LIKE (PRIMER ON SIDE). The last four labels are our competitors.
```````````````````````````````````````````````````````````````````````````````````````````````````
We need this label to look professional, sharp, eye catching and modern.
OUR PRIMARY COLORS ARE BLACK AND WHITE. IF YOU INCOPORATE ANOTHER COLOR, SILVER OR GOLD MIGHT BE IDEAL BUT PLEASE DON'T DRIFT TOO FAR.
The attached documents:
1st - Our Logo
2nd - Our chalk paint label (reference). We do not need a chalk paint label.
3rd. A random design example. I like the PRIME on the side running vertically. I think it's a cool design concept.
````````````````````````````````````````````````````````````````````````````````````````````````````
We are going to be using a normal paint can with a metal bail/handle so please use that with you design work
``````````````````````````````````````````````````````````````````````````````````````````````````
Order, in my head:
2743
Coatings
^^ I want this to stand out as well but I don't want it to be the first thing your eye is drawn to. Probably 2nd
Interior/Exterior
Multi - Surface Primer
^^ Want this to stick out and draw your eye so the customer knows what it is immediately
Exceptional Adhesion, Performance, Durability,
Use on Wood, Drywall, Plaster, Stucco, Masonry, Brick, Paneling, Painted Metal, & Properly Prepared Glossy Surfaces & More
35* Lowe Temperature Application (can be on side or small)
100% Acrylic
Low Odor - Low VOC - Soap & Water Clean Up
1 US Gallon - 3.785 L
Feel free to get creative with it!

```html
<!DOCTYPE html>
<html lang="en">
<head>
<meta charset="utf-8">
<title>2743 Coatings — Multi Surface Primer Label</title>
<link rel="stylesheet" href="https://fonts.googleapis.com/css2?family=Archivo+Black&family=Montserrat:wght@400;500&display=swap">
<style>
  :root {
    --ink: #000000;
    --paper: #ffffff;
    --page: #ffffff;
    --shadow: rgba(0, 0, 0, 0.55);
  }
  html, body {
    margin: 0;
    padding: 0;
    width: 1200px;
    height: 932px;
    overflow: hidden;
    background: var(--page);
  }
  .canvas {
    position: relative;
    width: 1200px;
    height: 932px;
  }
  .label {
    position: absolute;
    left: 264px;
    top: 112px;
    width: 745px;
    height: 689px;
    background: var(--paper);
    box-shadow: 4px 5px 5px var(--shadow);
    color: var(--ink);
  }
  .brand-name {
    position: absolute;
    left: 40px;
    top: 166px;
    width: 402px;
    margin: 0;
    text-align: center;
    font-family: "Montserrat", sans-serif;
    font-weight: 500;
    font-size: 30px;
    line-height: 36px;
    letter-spacing: 2px;
    color: var(--ink);
  }
  .resin {
    position: absolute;
    left: 50px;
    top: 383px;
    width: 160px;
    text-align: center;
    font-family: "Archivo Black", sans-serif;
    line-height: 1.25;
  }
  .resin-pct { display: block; font-size: 20px; letter-spacing: 1px; }
  .resin-type { display: block; font-size: 23px; letter-spacing: 1.5px; }
  .divider {
    position: absolute;
    left: 212px;
    top: 332px;
    width: 2px;
    height: 112px;
    background: var(--ink);
  }
  .benefits {
    position: absolute;
    left: 227px;
    top: 378px;
    margin: 0;
    padding: 0;
    list-style: none;
    font-family: "Montserrat", sans-serif;
    font-weight: 400;
    font-size: 18px;
    line-height: 23px;
    letter-spacing: 0.4px;
  }
  .surfaces {
    position: absolute;
    left: 20px;
    top: 478px;
    width: 450px;
    margin: 0;
    text-align: center;
    font-family: "Montserrat", sans-serif;
    font-size: 13.5px;
    line-height: 17.6px;
    letter-spacing: 0.4px;
  }
  .surfaces strong {
    font-weight: 500;
    font-size: 16px;
  }
  .volume {
    position: absolute;
    left: 40px;
    top: 636px;
    width: 392px;
    text-align: center;
    font-family: "Archivo Black", sans-serif;
    font-size: 17px;
    line-height: 22px;
    letter-spacing: 1.5px;
  }
  .side-panel {
    position: absolute;
    left: 0;
    top: 0;
    width: 745px;
    height: 689px;
    overflow: visible;
  }
  .panel-fill { fill: var(--ink); }
  .product-main {
    font-family: "Archivo Black", sans-serif;
    font-size: 104px;
    fill: var(--paper);
  }
  .product-sub {
    font-family: "Archivo Black", sans-serif;
    font-size: 56px;
    fill: var(--paper);
  }
  .product-notes {
    font-family: "Montserrat", sans-serif;
    font-size: 13.5px;
    fill: var(--paper);
  }
  .temp-note {
    font-family: "Montserrat", sans-serif;
    font-size: 13.5px;
    letter-spacing: 0.3px;
    fill: var(--paper);
  }
</style>
</head>
<body>
<div class="canvas">
  <div class="label">
    <p class="brand-name">2743 COATINGS</p>

    <div class="resin">
      <span class="resin-pct">100%</span>
      <span class="resin-type">ACRYLIC</span>
    </div>
    <div class="divider"></div>
    <ul class="benefits">
      <li>Exceptional Adhesion</li>
      <li>Performance</li>
      <li>Durability</li>
    </ul>

    <p class="surfaces"><strong>Use</strong> on Wood, Drywall, Plaster, Stucco, Masonry,<br>Brick, Paneling, Painted Metal, &amp; Properly Prepared<br>Glossy Surfaces &amp; More</p>

    <div class="volume">1 US GALLON - 3.785 L</div>

    <svg class="side-panel" width="745" height="689" viewBox="0 0 745 689">
      <polygon class="panel-fill" points="539,-3 745,-3 745,689 426,689"/>
      <text class="product-main" transform="translate(603,609) rotate(-90)" textLength="333" lengthAdjust="spacingAndGlyphs">MULTI</text>
      <text class="product-sub" transform="translate(669,612) rotate(-90)" textLength="524" lengthAdjust="spacingAndGlyphs">SURFACE PRIMER</text>
      <text class="product-notes" transform="translate(706,552) rotate(-90)" textLength="373" lengthAdjust="spacingAndGlyphs">Low Odor - Low VOC - Soap &amp; Water Clean Up</text>
      <text class="temp-note" x="595" y="658" text-anchor="middle">35* Lowe Temperature Application</text>
    </svg>
  </div>
</div>
</body>
</html>
```